Create a flyer design (10cm X 21cm) for an aquarium in France

We are a public aquarium in France and we want announcing the events of christmas holidays
We invite you to create our flyer recto (just the front side).

The size of this flyer is : 10cm X 21cm
Have a look on flyer.doc to know texts...
We want also get the flyer in original version (.psd, .ai) please.

We remain at your disposal for any question.
Thanks.

Industry/Entity Type

Events

Requirements
Must have
• The text must be written in french, you will find attached all the text that you have to fill in the flyer.
• You also have to use our logo in the top or in the bottom of the flyer (2 versions of the logo four color or black and white version. According your design you can use one of them)
• You must specify our website and our adress.
• Have a look on flyer.doc to know texts...

```html
<!DOCTYPE html>
<html lang="fr">
<head>
<meta charset="utf-8">
<title>Vos vacances de Noël à l'aquarium</title>
<link rel="stylesheet" href="https://fonts.googleapis.com/css2?family=Roboto+Slab:wght@700;800&family=Arimo:wght@400;700&display=swap">
<style>
  :root {
    --red-deep: #8e0d12;
    --red: #c41a1f;
    --red-glow: #e0322c;
    --lime: #c9d62a;
    --lime-soft: #dfe77a;
    --white: #ffffff;
    --pine: #1f5a2a;
    --pine-light: #3d8a3a;
  }
  * { margin: 0; padding: 0; box-sizing: border-box; }
  html, body { width: 1200px; height: 2539px; overflow: hidden; background: var(--red-deep); }
  .flyer {
    position: relative;
    width: 1200px;
    height: 2539px;
    overflow: hidden;
    background: radial-gradient(ellipse 80% 55% at 50% 42%, var(--red-glow) 0%, var(--red) 45%, var(--red-deep) 100%);
    font-family: "Arimo", Arial, sans-serif;
    color: var(--white);
  }
  .garland {
    position: absolute; left: 0; top: 0; width: 1200px; height: 120px;
    background: linear-gradient(180deg, var(--pine) 0%, var(--pine-light) 60%, rgba(61,138,58,0) 100%);
  }
  .headline {
    position: absolute; left: 0; top: 190px; width: 1200px; text-align: center;
    font-family: "Roboto Slab", Georgia, serif; font-weight: 800;
    text-shadow: 0 0 18px rgba(255,255,255,.55);
  }
  .headline__lead { display: block; font-size: 70px; line-height: 1; letter-spacing: -1px; }
  .headline__main { display: block; font-size: 178px; line-height: 1; margin-top: 2px; letter-spacing: -2px; }
  .photo {
    position: absolute; border-radius: 50%;
    border: 26px solid var(--lime);
    box-shadow: 0 0 0 6px var(--lime-soft);
  }
  .photo--diver { left: 30px; top: 760px; width: 370px; height: 370px;
    background: radial-gradient(circle at 40% 40%, #4fb2b0, #1d6f74 70%, #0f3f44); }
  .photo--grouper { left: 400px; top: 535px; width: 380px; height: 380px;
    background: radial-gradient(circle at 45% 45%, #8a5a4a, #3e3a52 60%, #1d2436); }
  .photo--angelfish { left: 800px; top: 730px; width: 420px; height: 420px;
    background: radial-gradient(circle at 45% 50%, #2a3470, #1b2446 60%, #0f1628); }
  .photo--spotted { left: 370px; top: 960px; width: 420px; height: 420px;
    background: radial-gradient(circle at 50% 50%, #8d8f88, #4e524d 60%, #2a2d2a); }
  .programme {
    position: absolute; left: 0; top: 1452px; width: 1200px; text-align: center;
    font-weight: 700; font-size: 33px; line-height: 42px;
  }
  .programme__item { margin-bottom: 34px; }
  .programme__item--tight { margin-bottom: 8px; }
  .contact {
    position: absolute; left: 0; top: 2225px; width: 1200px; height: 280px;
  }
  .brand {
    position: absolute; left: 70px; top: 60px; width: 440px;
    font-family: "Arimo", Arial, sans-serif; font-weight: 700;
    font-size: 66px; line-height: 66px; color: var(--white);
  }
  .divider { position: absolute; left: 545px; top: 14px; width: 3px; height: 250px; background: var(--white); }
  .contact__info { position: absolute; left: 582px; top: 20px; font-size: 28px; line-height: 36px; }
  .contact__phone { font-weight: 700; font-size: 48px; line-height: 60px; margin-top: 8px; }
  .contact__web { font-weight: 700; font-size: 38px; line-height: 46px; }
</style>
</head>
<body>
<main class="flyer">
  <div class="garland" role="img" aria-label="Guirlande de sapin avec houx et boules de Noël"></div>

  <h1 class="headline">
    <span class="headline__lead">Vos vacances de Noël à l’</span>
    <span class="headline__main">aquarium</span>
  </h1>

  <div class="photo photo--diver" role="img" aria-label="Plongeur déguisé en Père Noël dans le bassin, observé par des enfants"></div>
  <div class="photo photo--grouper" role="img" aria-label="Poisson tacheté aux couleurs vives"></div>
  <div class="photo photo--angelfish" role="img" aria-label="Poisson-ange bleu foncé avec une tache jaune"></div>
  <div class="photo photo--spotted" role="img" aria-label="Poisson gris à taches noires sur le fond du bassin"></div>

  <section class="programme">
    <p class="programme__item">Animations « bassin tactile<br>commentées plusieurs fois par jour</p>
    <p class="programme__item">Nourrissages commentés de nos espèces<br>aquatiques chaque après-midi</p>
    <p class="programme__item">Plongée du Père-Noël les 22 et 23 décembre</p>
    <p class="programme__item">Atelier scientifique sur les Requins lundi 28 décembre</p>
    <p class="programme__item">Nocturne, une visite drôle et décalée,<br>mardi 29 décembre</p>
    <p class="programme__item programme__item--tight">Fish manucure, les 29, 30 et 31 décembre<br>Dégustation vitaminée, les 2 et 3 janvier</p>
  </section>

  <footer class="contact">
    <div class="brand">Aquarium<br>de Kermor</div>
    <div class="divider"></div>
    <div class="contact__info">
      <p>14, rue des Mouettes<br>56000 KERMOR</p>
      <p class="contact__phone">02 97 00 12 34</p>
      <p>Retrouvez toutes les informations via</p>
      <p class="contact__web">aquariumdekermor.fr</p>
    </div>
  </footer>
</main>
</body>
</html>
```